Technology solutions catalog

Were looking for a catalogue to supplement our website and corporate branding.

Our website will give you a good understanding of our products and services as well as our theme.

Our base colour and logo is red, white and grey.

www.voltrane.com.au

The aim of the catalogue is to showcase our business IT services & solutions. This will be a mix of education about the new solutions available to small and medium business today and how these solutions can increase productivity.

We would also like tip sections

This isn't all about selling but also about educating SMB's of the new and exciting IT solutions available today and having them book a free consult with us to discuss further about how we can help the business.

Solutions and area's that the catalogue will need to cover include

Front Cover -
-About us section, with our business contact information (1st page)
- Introduction. (2nd page)
-Communication Solutions - this includes Email, IP phones and business IT networks (2 pages)
- Data & Storage solutions (2 pages)
- Hardware (1 pages)
- Business IT health check list (1 page)
- Services and support offering (2 pages)
- Software & Popular cloud solutions (2 pages)
- Website / E-commerce solutions (2 pages)
Back cover

Based on two pages per solution the whole catalogue will be around 14 pages.

We don't need any text content done. We would like Headings on pages including page numbers. Footer please.

We're looking for a template that we can have our designer finish off by adding in some further product and service image and text.

Thank you for your consideration

Target Market(s)

IT for small and medium businesses

Industry/Entity Type

Supplement

Requirements
Must have
• Size A4
• Design supplied in Adobe indesign so we can edit and add our text and content
• Clean design

```html
<!DOCTYPE html>
<html lang="en">
<head>
<meta charset="utf-8">
<title>Voltrane Catalogue – Website / E-commerce Solutions</title>
<link href="https://fonts.googleapis.com/css2?family=Lato:wght@300;400;700;900&display=swap" rel="stylesheet">
<style>
  :root {
    --backdrop: #262626;
    --paper: #ffffff;
    --brand-red: #b91f25;
    --body-grey: #8a8a8a;
    --footer-bg: #323232;
    --footer-text: #c9c9c9;
    --label-white: #ffffff;
  }
  * { margin: 0; padding: 0; box-sizing: border-box; }
  html, body {
    width: 984px; height: 1200px; overflow: hidden;
    background: var(--backdrop);
    font-family: "Lato", Arial, sans-serif;
  }
  .page-label {
    position: absolute; top: 53px; left: 0; width: 984px;
    text-align: center; color: var(--label-white);
    font-weight: 700; font-size: 20px;
  }
  .page {
    position: absolute; left: 158px; top: 109px;
    width: 683px; height: 967px;
    background: var(--paper);
  }
  .header-band {
    position: absolute; left: 0; top: 51px;
    width: 498px; height: 28px; background: var(--brand-red);
  }
  .brand-name {
    position: absolute; right: 32px; top: 50px;
    font-weight: 900; font-size: 27px; line-height: 30px;
    color: var(--brand-red); letter-spacing: 0.2px;
  }
  .page-title {
    position: absolute; left: 41px; top: 150px;
    font-weight: 300; font-size: 40px; line-height: 48px;
    color: var(--brand-red);
  }
  .service-icon {
    position: absolute; left: 59px;
    width: 120px; height: 120px; border-radius: 50%;
    background: var(--brand-red);
    display: flex; align-items: center; justify-content: center;
  }
  .service-block {
    position: absolute; left: 247px; width: 357px;
  }
  .service-heading {
    font-weight: 700; font-size: 16.5px; line-height: 20px;
    color: var(--brand-red); text-transform: uppercase;
    margin-bottom: 8px;
  }
  .service-text {
    font-size: 11.6px; line-height: 19.7px;
    color: var(--body-grey); text-align: justify;
  }
  .page-footer {
    position: absolute; left: 0; bottom: 0;
    width: 683px; height: 34px; background: var(--footer-bg);
    display: flex; align-items: center; justify-content: space-between;
    padding: 0 24px; font-size: 12px; color: var(--footer-text);
  }
</style>
</head>
<body>
  <div class="page-label">Page 15</div>

  <main class="page">
    <div class="header-band"></div>
    <div class="brand-name">Voltrane</div>

    <h1 class="page-title">Website / E-commerce Solutions</h1>

    <div class="service-icon" style="top:250px;">
      <svg width="64" height="56" viewBox="0 0 64 56" aria-hidden="true">
        <rect x="2" y="6" width="58" height="36" rx="2" fill="none" stroke="#fff" stroke-width="4"/>
        <rect x="26" y="42" width="10" height="6" fill="#fff"/>
        <rect x="18" y="48" width="26" height="4" rx="1" fill="#fff"/>
        <path d="M58 2 L62 5 L30 34 L27 31 Z" fill="#fff"/>
        <path d="M26 32 L29 35 C27 39 22 40 18 38 C21 37 22 34 26 32 Z" fill="#fff"/>
      </svg>
    </div>
    <section class="service-block" style="top:258px;">
      <h2 class="service-heading">Website Services</h2>
      <p class="service-text">Lorem ipsum dolor sit amet, consectetuer adipiscing elit, sed diam nonummy nibh euismod tincidunt ut laoreet dolore magna aliquam erat volutpat. Ut wisi enim ad minim veniam, quis nostrud exerci tation ullamcorper suscipit lobortis nisl ut aliquip ex ea commodo consequat. Duis autem vel eum iriure dolor in hendrerit in vulpu&shy;tate velit esse molestie consequat, vel illum dolore eu feugiat nulla facilisis at vero eros et accumsan et iusto odio dignissim qui blandit praesent luptatum zzril delenit augue duis dolore te feugait nulla facilisi. Nam liber tempor cum soluta nobis eleifend option congue nihil imperdiet doming id quod mazim placerat facer possim assum. Typi non habent claritatem insitam; est usus legentis in iis qui facit eorum claritatem. Investigationes demonstraverunt</p>
    </section>

    <div class="service-icon" style="top:596px;">
      <svg width="54" height="54" viewBox="0 0 54 54" aria-hidden="true" fill="#fff">
        <rect x="0" y="0" width="14" height="12"/><rect x="20" y="0" width="14" height="12"/><rect x="40" y="0" width="14" height="12"/>
        <rect x="0" y="20" width="14" height="12"/><rect x="20" y="20" width="14" height="12"/><rect x="40" y="20" width="14" height="12"/>
        <rect x="0" y="40" width="14" height="12"/><rect x="20" y="40" width="14" height="12"/><rect x="40" y="40" width="14" height="12"/>
      </svg>
    </div>
    <section class="service-block" style="top:601px;">
      <h2 class="service-heading">Websites Products</h2>
      <p class="service-text">Lorem ipsum dolor sit amet, consectetuer adipiscing elit, sed diam nonummy nibh euismod tincidunt ut laoreet dolore magna aliquam erat volutpat. Ut wisi enim ad minim veniam, quis nostrud exerci tation ullamcorper suscipit lobortis nisl ut aliquip ex ea commodo consequat. Duis autem vel eum iriure dolor in hendrerit in vulpu&shy;tate velit esse molestie consequat, vel illum dolore eu feugiat nulla facilisis at vero eros et accumsan et iusto odio dignissim qui blandit praesent luptatum zzril delenit augue duis dolore te feugait nulla facilisi. Nam liber tempor cum soluta nobis eleifend option congue nihil imperdiet doming id quod mazim placerat facer possim assum. Typi non habent claritatem insitam; est usus legentis in iis qui facit eorum claritatem. Investigationes demonstraverunt</p>
    </section>

    <footer class="page-footer">
      <span class="footer-page-number">Page 14</span>
      <span class="footer-web">www.voltrane.com.au</span>
    </footer>
  </main>
</body>
</html>
```